New florist business website design

Number 1 want is an easy to navigate & check out website
Needs to be beautiful and eye catching as well.
This is an online only business (no shop front)
Rustic and blush pinks, neutrals, woods, leaves
Customers need to be able to go onto my website, select something they want to buy but have the option to use a drop down box to change colours of the flowers, or add notes to make changes to the arrangement

Industry/Entity Type

Florist

Coding

Coded - Design and coding required

Number of Pages Required

5+ page

Colors
f9d9e8
fff2ec
fffefc

Requirements
Must have
• Drop down menu to take you to other pages for Arrangements, bouquets, everlasting arrangements, gifts, contact
Be able to purchase and “add to basket”
Checkout page
Nice to have
• Be able to add my own photos once I’ve taken new ones
Should not have
• Tacky images or clip art

```html
<!DOCTYPE html>
<html lang="en">
<head>
<meta charset="utf-8">
<title>Fern &amp; Folly — Florist</title>
<link href="https://fonts.googleapis.com/css2?family=Playfair+Display:wght@400;500&family=Great+Vibes&family=Montserrat:wght@400;500;600;700&display=swap" rel="stylesheet">
<style>
:root{
  --blush:#fcedf0;
  --blush-deep:#f9d9e8;
  --cream:#fff2ec;
  --paper:#fffefc;
  --ink:#2b2b2b;
  --ink-soft:#4a4a4a;
  --footer:#3b3a3a;
  --footer-text:#d9d9d9;
  --wood:#6b4a36;
  --sand:#f8dcc8;
}
*{box-sizing:border-box;margin:0;padding:0}
html,body{width:1200px;height:4073px;overflow:hidden}
body{position:relative;background:var(--blush);color:var(--ink);font-family:"Montserrat",sans-serif}
.abs{position:absolute}
.serif{font-family:"Playfair Display",serif}
.script{font-family:"Great Vibes",cursive;font-weight:400}
.photo{position:absolute}

/* header */
.header{left:0;top:0;width:1200px;height:110px;background:var(--blush)}
.callus{left:216px;top:16px;font-family:"Playfair Display",serif;font-size:12px;color:var(--ink-soft);display:flex;align-items:center;gap:6px}
.account{left:868px;top:16px;font-family:"Playfair Display",serif;font-size:12px;color:var(--ink-soft);display:flex;align-items:center;gap:6px}
.cart{left:1012px;top:10px}
.nav{top:56px;display:flex;gap:0;font-family:"Playfair Display",serif;font-size:15px;color:var(--ink)}
.nav a{color:inherit;text-decoration:none;display:flex;align-items:center;gap:4px}
.nav-left{left:216px;width:288px;justify-content:space-between;border-bottom:1px solid #bdbdbd;padding-bottom:10px}
.nav-right{left:706px;width:336px;justify-content:space-between;border-bottom:1px solid #bdbdbd;padding-bottom:10px}
.nav .active:after{content:"";position:absolute}
.logo{left:524px;top:0;width:152px;height:152px;border-radius:50%;background:var(--blush);display:flex;align-items:center;justify-content:center;z-index:3}
.logo span{font-family:"Playfair Display",serif;font-size:20px;color:var(--ink-soft)}

/* hero */
.hero{left:0;top:110px;width:1200px;height:536px;background:linear-gradient(90deg,#7d8c5b 0%,#a8626b 14%,#5c3b2a 30%,#6a4630 50%,#5a3a28 70%,#546b46 86%,#c8b34e 100%)}
.hero-shade{left:296px;top:240px;width:608px;height:276px;background:rgba(60,36,24,.45)}
.hero-script{left:0;width:1200px;top:270px;text-align:center;font-size:66px;color:#fff}
.hero-title{left:0;width:1200px;top:355px;text-align:center;font-family:"Playfair Display",serif;font-size:54px;color:#fff;letter-spacing:1px}
.btn{position:absolute;display:flex;align-items:center;justify-content:center;font-family:"Playfair Display",serif;font-size:14px;gap:6px;text-decoration:none}
.btn-sand{background:var(--sand);color:var(--ink)}
.btn-ghost-light{border:2px solid #fff;color:#fff}
.btn-ghost-dark{border:2px solid var(--ink);color:var(--ink)}
.arrow-circle{width:34px;height:34px;border-radius:50%;background:rgba(255,255,255,.85);display:flex;align-items:center;justify-content:center}

/* features */
.features{left:0;top:646px;width:1200px;height:336px;background:#fff}
.feature{position:absolute;top:60px;width:300px;text-align:center}
.feature h3{font-family:"Playfair Display",serif;font-weight:400;font-size:16px;margin-top:20px;letter-spacing:.3px}
.feature p{font-size:12px;line-height:22px;margin-top:14px;color:var(--ink-soft)}

/* section titles */
.sec-script{left:0;width:1200px;text-align:center;font-size:50px;color:var(--ink-soft)}
.sec-title{left:0;width:1200px;text-align:center;font-family:"Playfair Display",serif;font-size:34px;font-weight:400;letter-spacing:.5px}

/* products */
.product{position:absolute;top:1202px;width:230px;text-align:center}
.product .img{height:290px}
.product h4{font-family:"Playfair Display",serif;font-weight:400;font-size:17px;margin-top:18px}
.product .price{font-size:17px;margin-top:8px}

/* perfect spot */
.spot-frame{left:522px;top:1657px;width:574px;height:515px;border:2px solid var(--ink);padding:8px;background:var(--blush)}
.spot-card{left:111px;top:1715px;width:537px;height:399px;background:#fff;box-shadow:0 2px 10px rgba(0,0,0,.06);text-align:center}
.spot-card .script{font-size:48px;margin-top:28px;color:var(--ink-soft)}
.spot-card h2{font-family:"Playfair Display",serif;font-weight:400;font-size:32px;margin-top:-4px}
.spot-card p{font-size:12px;line-height:22px;color:var(--ink-soft);width:446px;margin:16px auto 0}

/* perfect choice band */
.choice{left:0;top:2268px;width:1200px;height:343px;background:linear-gradient(90deg,#2f3a36 0%,#455040 30%,#6d6a63 55%,#3a4037 80%,#2d332e 100%)}
.choice-frame{left:18px;top:2284px;width:1164px;height:311px;border:2px solid #fff}

/* gallery */
.g-frame{position:absolute;border:2px solid var(--ink);padding:8px}
.g-frame .photo{position:static;width:100%;height:100%}

/* testimonial */
.quote{left:285px;top:3412px;width:630px;text-align:center;font-size:12.5px;line-height:24px;font-style:italic;color:var(--ink-soft)}
.quote-name{left:0;width:1200px;top:3556px;text-align:center;font-size:14px;font-weight:600}

/* footer */
.footer{left:0;top:3675px;width:1200px;height:398px;background:var(--footer);color:var(--footer-text)}
.f-col{position:absolute;top:78px}
.f-col h5{font-size:17px;font-weight:600;color:#fff;margin-bottom:26px}
.f-col ul{list-style:none}
.f-col li{font-size:12.5px;line-height:22px;display:flex;gap:10px;align-items:flex-start}
.f-col li .chev{font-size:11px}
.f-input{width:262px;height:42px;background:#4a4949;font-size:12px;color:#bbb;padding:14px 22px}
.f-subscribe{width:130px;height:42px;background:#fff;color:var(--ink);font-size:12px;font-weight:700;display:flex;align-items:center;justify-content:center;margin-top:16px}
.copyright{left:0;width:1200px;top:290px;text-align:center;font-size:14px;color:#fff}
.cards{left:428px;top:340px;display:flex;gap:9px}
.cards span{width:45px;height:28px;border-radius:3px;display:block}
</style>
</head>
<body>

<!-- header -->
<header class="abs header">
  <div class="abs callus">
    <svg width="12" height="12" viewBox="0 0 24 24"><path d="M6.6 10.8a15 15 0 0 0 6.6 6.6l2.2-2.2a1 1 0 0 1 1-.25 11.4 11.4 0 0 0 3.6.57 1 1 0 0 1 1 1V20a1 1 0 0 1-1 1A17 17 0 0 1 3 4a1 1 0 0 1 1-1h3.5a1 1 0 0 1 1 1c0 1.25.2 2.45.57 3.57a1 1 0 0 1-.25 1z" fill="#333"/></svg>
    Call us : +1 888 888 8888
  </div>
  <nav class="abs nav nav-left">
    <a href="#" class="active" style="position:relative">Home
      <svg style="position:absolute;left:14px;top:30px" width="10" height="6" viewBox="0 0 10 6"><path d="M0 6L5 0L10 6z" fill="#999"/></svg></a>
    <a href="#">Arrangements <svg width="9" height="6" viewBox="0 0 9 6"><path d="M1 1l3.5 3.5L8 1" stroke="#333" fill="none" stroke-width="1.3"/></svg></a>
    <a href="#">Bouquets <svg width="9" height="6" viewBox="0 0 9 6"><path d="M1 1l3.5 3.5L8 1" stroke="#333" fill="none" stroke-width="1.3"/></svg></a>
  </nav>
  <div class="abs logo"><span>Fern &amp; Folly</span></div>
  <div class="abs account">
    <svg width="12" height="12" viewBox="0 0 24 24"><circle cx="12" cy="8" r="4.5" stroke="#333" stroke-width="2" fill="none"/><path d="M3 22c0-5 4-8 9-8s9 3 9 8" stroke="#333" stroke-width="2" fill="none"/></svg>
    My account
  </div>
  <div class="abs cart">
    <svg width="36" height="26" viewBox="0 0 36 26"><path d="M3 8h16l-1.5 16h-13z" stroke="#333" stroke-width="1.3" fill="none"/><path d="M7 10V6a4 4 0 0 1 8 0v4" stroke="#333" stroke-width="1.3" fill="none"/><circle cx="23" cy="11" r="7" fill="#f4c6d6"/><text x="23" y="14.5" text-anchor="middle" font-size="10" font-family="Montserrat,sans-serif" fill="#333">1</text></svg>
  </div>
  <nav class="abs nav nav-right">
    <a href="#">Everlasting arrangements <svg width="9" height="6" viewBox="0 0 9 6"><path d="M1 1l3.5 3.5L8 1" stroke="#333" fill="none" stroke-width="1.3"/></svg></a>
    <a href="#">Gifts <svg width="9" height="6" viewBox="0 0 9 6"><path d="M1 1l3.5 3.5L8 1" stroke="#333" fill="none" stroke-width="1.3"/></svg></a>
    <a href="#">Contact</a>
  </nav>
</header>

<!-- hero -->
<section class="abs hero photo" role="img" aria-label="Florist hands wrapping a bouquet on a wooden table surrounded by roses, tulips, twine and ribbon"></section>
<div class="abs hero-shade"></div>
<div class="abs hero-script script">Welcome to</div>
<h1 class="abs hero-title">PERFECT BOUQUET</h1>
<a class="btn btn-sand" href="#" style="left:459px;top:433px;width:133px;height:40px">Shop now</a>
<a class="btn btn-ghost-light" href="#" style="left:604px;top:433px;width:134px;height:40px">Read more
  <svg width="14" height="8" viewBox="0 0 14 8"><path d="M0 4h12M9 1l3 3-3 3" stroke="#fff" stroke-width="1.6" fill="none"/></svg></a>
<div class="abs arrow-circle" style="left:38px;top:361px"><svg width="10" height="14" viewBox="0 0 10 14"><path d="M7 2L2 7l5 5" stroke="#333" stroke-width="1.6" fill="none"/></svg></div>
<div class="abs arrow-circle" style="left:1126px;top:361px"><svg width="10" height="14" viewBox="0 0 10 14"><path d="M3 2l5 5-5 5" stroke="#333" stroke-width="1.6" fill="none"/></svg></div>

<!-- features -->
<section class="abs features">
  <div class="feature" style="left:124px">
    <svg width="66" height="66" viewBox="0 0 66 66" fill="none" stroke="#333" stroke-width="2">
      <circle cx="33" cy="33" r="7"/>
      <circle cx="33" cy="17" r="10"/><circle cx="48" cy="28" r="10"/><circle cx="42" cy="46" r="10"/><circle cx="24" cy="46" r="10"/><circle cx="18" cy="28" r="10"/>
    </svg>
    <h3>READY TO BE IMPRESSED</h3>
    <p>Lorem ipsum dolor sit amet, consecte tur<br>adipiscing elitin uta</p>
  </div>
  <div class="feature" style="left:450px">
    <svg width="66" height="66" viewBox="0 0 66 66" fill="none" stroke="#333" stroke-width="2">
      <circle cx="33" cy="14" r="8"/><circle cx="20" cy="22" r="8"/><circle cx="46" cy="22" r="8"/><circle cx="33" cy="28" r="7"/>
      <path d="M22 34l11 30 11-30"/><path d="M28 42h10"/>
    </svg>
    <h3>POWERFUL SOLUTIONS</h3>
    <p>Lorem ipsum dolor sit amet, consecte tur<br>adipiscing elitin uta</p>
  </div>
  <div class="feature" style="left:776px">
    <svg width="70" height="66" viewBox="0 0 70 66" fill="none" stroke="#333" stroke-width="2">
      <path d="M35 58C20 50 8 38 8 16c14 2 24 14 27 42z"/><path d="M35 58C50 50 62 38 62 16c-14 2-24 14-27 42z"/>
      <path d="M35 58V20"/><circle cx="35" cy="14" r="7"/>
    </svg>
    <h3>LEADERS OF TOMORROW</h3>
    <p>Lorem ipsum dolor sit amet, consecte tur<br>adipiscing elitin uta</p>
  </div>
</section>

<!-- arrangements -->
<div class="abs sec-script script" style="top:1050px">Wonderful gift</div>
<h2 class="abs sec-title" style="top:1128px">OUR WONDERFUL ARRANGEMENTS</h2>

<div class="product" style="left:111px">
  <div class="img photo" style="position:static;background:linear-gradient(160deg,#c9d2c4,#eddcd3 55%,#a9b8a7)" role="img" aria-label="Peach and white rose bouquet held in hands"></div>
  <h4>ORANGE SILKA</h4><div class="price">$330</div>
</div>
<div class="product" style="left:360px">
  <div class="img photo" style="position:static;background:linear-gradient(160deg,#c7a27b,#d6826f 50%,#b38a63)" role="img" aria-label="Red and pink flower bunch being trimmed on a wooden table"></div>
  <h4>DARK FOREST</h4><div class="price">$330</div>
</div>
<div class="product" style="left:609px">
  <div class="img photo" style="position:static;background:linear-gradient(160deg,#b8c1c7,#6d6477 50%,#a7b0b6)" role="img" aria-label="Dried protea and lavender bouquet held in hands"></div>
  <h4>PEARL ROSES</h4><div class="price">$330</div>
</div>
<div class="product" style="left:858px">
  <div class="img photo" style="position:static;background:linear-gradient(170deg,#7f9a6c,#e9e26a 40%,#b8bcc0 80%)" role="img" aria-label="White and yellow daisies in a metal pot on a lace doily"></div>
  <h4>RUSTIC DECOR</h4><div class="price">$330</div>
</div>

<!-- perfect spot -->
<div class="photo" role="img" aria-label="Line-drawn floral branch" style="left:14px;top:1608px;width:312px;height:264px;background:radial-gradient(ellipse at 40% 50%,rgba(80,80,80,.08),transparent 70%)"></div>
<div class="abs spot-frame">
  <div class="photo" role="img" aria-label="Wedding couple under a draped tent with flower arch" style="position:static;width:100%;height:100%;background:linear-gradient(180deg,#e8dccf 0%,#d8c7b4 40%,#8d8a82 75%,#b7b2ab 100%)"></div>
</div>
<div class="abs spot-card">
  <div class="script">Wonderful gift</div>
  <h2>A PERFECT SPOT</h2>
  <p>Lorem ipsum dolor sit amet, consectetur adipiscing elit, sed do eiusmod tempor incididunt ut labore et dolore magna aliqua. Ut enim ad minim veniam, quis nostrud exercitation ullamco laboris nisi ut aliquip ex ea commodo consequat. Duis aute irure dolor in reprehenderit in voluptate velit esse cillum dolore eu fugiat</p>
</div>
<a class="btn btn-ghost-dark" href="#" style="left:313px;top:2015px;width:134px;height:42px;background:#fff">Read more
  <svg width="14" height="8" viewBox="0 0 14 8"><path d="M0 4h12M9 1l3 3-3 3" stroke="#2b2b2b" stroke-width="1.6" fill="none"/></svg></a>
<div class="photo" role="img" aria-label="Blush pampas and dried flower spray" style="left:1020px;top:2070px;width:180px;height:180px;background:radial-gradient(circle at 55% 50%,rgba(236,180,180,.75),rgba(246,214,206,.4) 50%,transparent 72%)"></div>

<!-- perfect choice -->
<section class="abs choice photo" role="img" aria-label="Smiling florist arranging flowers in a bright flower shop"></section>
<div class="abs choice-frame"></div>
<div class="abs sec-script script" style="top:2338px;color:#fff;font-size:46px">For flower lovers</div>
<h2 class="abs sec-title" style="top:2410px;color:#fff;font-size:32px">PERFECT CHOICE</h2>
<a class="btn btn-ghost-light" href="#" style="left:532px;top:2477px;width:135px;height:38px">Read more
  <svg width="14" height="8" viewBox="0 0 14 8"><path d="M0 4h12M9 1l3 3-3 3" stroke="#fff" stroke-width="1.6" fill="none"/></svg></a>

<!-- gallery -->
<div class="g-frame" style="left:110px;top:2716px;width:308px;height:452px">
  <div class="photo" role="img" aria-label="Wrapped bouquet of roses and baby's breath held out" style="background:linear-gradient(165deg,#cfb7a8,#a996a6 45%,#c8a6a0 70%,#e8dede)"></div>
</div>
<div class="g-frame" style="left:445px;top:2716px;width:308px;height:214px">
  <div class="photo" role="img" aria-label="Bride holding a coral and pink rose bouquet" style="background:linear-gradient(160deg,#d8d4cf,#e99a88 50%,#cfcac3)"></div>
</div>
<div class="g-frame" style="left:445px;top:2955px;width:308px;height:213px">
  <div class="photo" role="img" aria-label="Colourful gerbera and chrysanthemum flowers" style="background:linear-gradient(135deg,#c84a6a,#e88a3c 35%,#8a4d9a 65%,#e5d9de)"></div>
</div>
<div class="g-frame" style="left:780px;top:2716px;width:308px;height:452px">
  <div class="photo" role="img" aria-label="Bride and groom outdoors with a pastel bouquet" style="background:linear-gradient(170deg,#d3c7b4,#b9a88e 40%,#5f6470 70%,#e8e2dc)"></div>
</div>
<a class="btn btn-ghost-dark" href="#" style="left:532px;top:3197px;width:134px;height:40px">View more
  <svg width="14" height="8" viewBox="0 0 14 8"><path d="M0 4h12M9 1l3 3-3 3" stroke="#2b2b2b" stroke-width="1.6" fill="none"/></svg></a>

<div class="photo" role="img" aria-label="Blush dried flower spray" style="left:0;top:3170px;width:190px;height:190px;background:radial-gradient(circle at 45% 50%,rgba(236,176,180,.75),rgba(246,214,206,.4) 50%,transparent 72%)"></div>
<div class="photo" role="img" aria-label="Blush dried flower spray" style="left:1010px;top:3480px;width:190px;height:190px;background:radial-gradient(circle at 55% 50%,rgba(236,176,180,.75),rgba(246,214,206,.4) 50%,transparent 72%)"></div>

<!-- testimonials -->
<div class="abs sec-script script" style="top:3290px;font-size:46px">For flower lovers</div>
<h2 class="abs sec-title" style="top:3352px;font-size:32px">OUR HAPPY CUSTOMERS</h2>
<svg class="abs" style="left:110px;top:3434px" width="26" height="44" viewBox="0 0 26 44"><path d="M22 2L4 22l18 20" stroke="#2b2b2b" stroke-width="2.4" fill="none"/></svg>
<svg class="abs" style="left:1064px;top:3434px" width="26" height="44" viewBox="0 0 26 44"><path d="M4 2l18 20L4 42" stroke="#2b2b2b" stroke-width="2.4" fill="none"/></svg>
<p class="abs quote">“Lorem ipsum dolor sit amet, consectetur adipiscing elit, sed do eiusmod tempor incididunt ut labore et dolore magna aliqua. Ut enim ad minim veniam, quis nostrud exercitation ullamco laboris nisi ut aliquip ex ea commodo consequat. Duis aute irure dolor in reprehenderit in voluptate velit esse cillum dolore eu fugiat nulla pariatur. Excepteur sint occaecat cupidatat non proident, sunt in culpa qui officia deserunt mollit anim id est laborum.”</p>
<div class="abs quote-name">Clara Benton</div>

<!-- footer -->
<footer class="abs footer">
  <div class="f-col" style="left:110px">
    <h5>Product info</h5>
    <ul>
      <li><span class="chev">»</span>Payment method</li>
      <li><span class="chev">»</span>Faq</li>
      <li><span class="chev">»</span>Shipping &amp; Delivery</li>
      <li><span class="chev">»</span>Refunds &amp; Return policy</li>
      <li><span class="chev">»</span>Truck your Order</li>
    </ul>
  </div>
  <div class="f-col" style="left:362px">
    <h5>Quick Links</h5>
    <ul>
      <li><span class="chev">»</span>Home</li>
      <li><span class="chev">»</span>About</li>
      <li><span class="chev">»</span>Product</li>
      <li><span class="chev">»</span>Reviews</li>
      <li><span class="chev">»</span>Contact us</li>
    </ul>
  </div>
  <div class="f-col" style="left:562px">
    <h5>Contact info</h5>
    <ul>
      <li><svg width="10" height="14" viewBox="0 0 10 14" style="margin-top:3px"><path d="M5 0a5 5 0 0 1 5 5c0 4-5 9-5 9S0 9 0 5a5 5 0 0 1 5-5z" fill="#d9d9d9"/><circle cx="5" cy="5" r="1.8" fill="#3b3a3a"/></svg><span>123, Lorem ipsum dolor sit<br>amet, consectetur</span></li>
      <li style="margin-top:22px"><svg width="11" height="11" viewBox="0 0 24 24" style="margin-top:5px"><path d="M6.6 10.8a15 15 0 0 0 6.6 6.6l2.2-2.2a1 1 0 0 1 1-.25 11.4 11.4 0 0 0 3.6.57 1 1 0 0 1 1 1V20a1 1 0 0 1-1 1A17 17 0 0 1 3 4a1 1 0 0 1 1-1h3.5a1 1 0 0 1 1 1c0 1.25.2 2.45.57 3.57a1 1 0 0 1-.25 1z" fill="#d9d9d9"/></svg>Phone : +1 888 888 8888</li>
      <li><svg width="12" height="10" viewBox="0 0 12 10" style="margin-top:6px"><rect width="12" height="10" rx="1" fill="#d9d9d9"/><path d="M0 1l6 4 6-4" stroke="#3b3a3a" fill="none"/></svg>Email : info@company.com</li>
    </ul>
  </div>
  <div class="f-col" style="left:825px">
    <h5>Newsletter</h5>
    <div class="f-input">Email address</div>
    <div class="f-subscribe">SUBSCRIBE</div>
  </div>
  <div class="abs copyright">© Copyrights 2021 Company name | All Rights Reserved</div>
  <div class="abs cards" aria-label="Accepted payment methods">
    <span style="background:#f2f2f2"></span>
    <span style="background:#f4efe9"></span>
    <span style="background:#2e77bb"></span>
    <span style="background:#e9eef5"></span>
    <span style="background:#e0442a"></span>
    <span style="background:#1d1d1d;border:1px solid #f0c419"></span>
  </div>
</footer>

</body>
</html>
```